Business Card for a finance professional

I need a business card design to introduce myself to a professional networking (mainly banks) and potential companies to hire and remember me. I would like to use black, grey, white and maybe gold/silver colors and maybe something with my initials(R L F P T). The final design should communicate seriousness, profissionalism and something innovative.

The basic informations in the card are: Name, e-mail, phone number and trabnet. (I'm thinking to put some directly short link to my trabnet account or maybe some app - non QR Code - to add my contacts to a phone directly.)

My name is Mariana Lopes Ferreira Pinto dos Reis (I prefer to use only 'Mariana Lopes' or 'Mariana Reis' but i'm open to other suggestions) and I have 26 years old (just if it helps to build based in my age).
Updates

Dear designers, I wish to thank your participation in this project! It was very difficult to choose one! Thank your for your work! Best regards and success. Mariana

Target Market(s)

Potential hires and big companies.

Industry/Entity Type

Finance

Requirements
Must have
• The informations required at the business card are:
Name: Mariana Lopes F. P. dos Reis
Email: mariana.lop.reis@quellomail.com
Phone: +55 61 8493 5710
TrabNet: http://br.trabnet-perfis.com/in/marianalr/
Nice to have
• Modern and innovative look.
I suggest to use the colors black, grey, white, gold and/or silver, but I'm open to other colors.
Should not have
• A message showing that I need to be hired. It's more to "know me and remember me" than "hire me please".

```html
<!DOCTYPE html>
<html lang="en">
<head>
<meta charset="utf-8">
<title>Mariana Lopes – Business Card</title>
<link href="https://fonts.googleapis.com/css2?family=Lobster+Two:ital,wght@1,700&family=Alegreya:wght@400;500&display=swap" rel="stylesheet">
<style>
  :root {
    --canvas: #1c1c1c;
    --ink-black: #050505;
    --ink-deep: #2b2b2b;
    --paper: #ffffff;
    --paper-shade: #eeeeee;
    --script-on-dark: #707070;
    --script-on-light: #cfcfcf;
    --tab-text-dark: #111111;
    --tab-text-light: #ffffff;
    --rule: #bdbdbd;
  }
  * { margin: 0; padding: 0; box-sizing: border-box; }
  html, body { width: 1200px; height: 1000px; overflow: hidden; background: var(--canvas); }
  .canvas {
    position: relative; width: 1200px; height: 1000px;
    display: grid; grid-template-columns: 520px 520px; grid-template-rows: 297px 297px;
    gap: 80px 60px; justify-content: center; align-content: center;
  }
  .card { position: relative; width: 520px; height: 297px; overflow: hidden; }
  .card--dark {
    background: linear-gradient(160deg, var(--ink-deep) 0%, var(--ink-black) 45%, var(--ink-black) 70%, #1a1a1a 100%);
  }
  .card--light { background: var(--paper); }
  .card__texture {
    position: absolute; inset: 0;
    background: linear-gradient(160deg, var(--paper) 0%, var(--paper-shade) 100%);
  }
  .script-name {
    position: absolute; font-family: "Lobster Two", cursive; font-style: italic; font-weight: 700;
    letter-spacing: 1px; white-space: nowrap;
  }
  .card--dark .script-name { color: var(--script-on-dark); }
  .card--light .script-name { color: var(--script-on-light); }
  .card--front .script-name { font-size: 64px; left: 50%; top: 50%; transform: translate(-50%, -50%); }
  .card--back .script-name { font-size: 58px; left: 28px; bottom: 26px; }

  .name-tab {
    position: absolute; left: 0; top: 44px; height: 40px; padding: 0 26px 0 24px;
    border-radius: 0 20px 20px 0; display: flex; align-items: center;
    font-family: "Alegreya", serif; font-size: 19px; font-weight: 500; letter-spacing: .3px;
  }
  .card--dark .name-tab { background: var(--paper); color: var(--tab-text-dark); }
  .card--light .name-tab { background: var(--ink-black); color: var(--tab-text-light); }

  .contact {
    position: absolute; right: 18px; top: 118px; padding-left: 12px;
    border-left: 1px solid var(--rule); list-style: none;
    font-family: "Alegreya", serif; font-size: 12.5px; line-height: 1;
  }
  .card--dark .contact { color: var(--paper); }
  .card--light .contact { color: var(--ink-black); border-left-color: var(--ink-black); }
  .contact__item { display: flex; align-items: center; gap: 7px; margin: 0 0 9px; }
  .contact__icon { width: 12px; height: 12px; flex: none; }
  .contact__mark { width: 10px; height: 10px; flex: none; background: currentColor; }
</style>
</head>
<body>
<main class="canvas">

  <section class="card card--dark card--back" aria-label="Business card back, black">
    <div class="name-tab">Mariana Lopes F. P. dos Reis</div>
    <ul class="contact">
      <li class="contact__item">
        <svg class="contact__icon" viewBox="0 0 12 12"><rect x="0.5" y="2" width="11" height="8" fill="none" stroke="currentColor"/><path d="M0.5 2 L6 7 L11.5 2" fill="none" stroke="currentColor"/></svg>
        mariana.lop.reis@quellomail.com
      </li>
      <li class="contact__item">
        <svg class="contact__icon" viewBox="0 0 12 12"><rect x="3" y="0.5" width="6" height="11" rx="1" fill="none" stroke="currentColor"/><line x1="5" y1="9.5" x2="7" y2="9.5" stroke="currentColor"/></svg>
        +55 61 8493 5710
      </li>
      <li class="contact__item">
        <span class="contact__mark"></span>
        TrabNet /marianalr
      </li>
    </ul>
    <div class="script-name">Mariana Lopes</div>
  </section>

  <section class="card card--dark card--front" aria-label="Business card front, black">
    <div class="script-name">Mariana Lopes</div>
  </section>

  <section class="card card--light card--front" aria-label="Business card front, white">
    <div class="card__texture" role="img" aria-label="Fine grid of small grey plus marks across the card"></div>
    <div class="script-name">Mariana Lopes</div>
  </section>

  <section class="card card--light card--back" aria-label="Business card back, white">
    <div class="card__texture" role="img" aria-label="Fine grid of small grey plus marks across the card"></div>
    <div class="name-tab">Mariana Lopes F. P. dos Reis</div>
    <ul class="contact">
      <li class="contact__item">
        <svg class="contact__icon" viewBox="0 0 12 12"><rect x="0.5" y="2" width="11" height="8" fill="none" stroke="currentColor"/><path d="M0.5 2 L6 7 L11.5 2" fill="none" stroke="currentColor"/></svg>
        mariana.lop.reis@quellomail.com
      </li>
      <li class="contact__item">
        <svg class="contact__icon" viewBox="0 0 12 12"><rect x="3" y="0.5" width="6" height="11" rx="1" fill="none" stroke="currentColor"/><line x1="5" y1="9.5" x2="7" y2="9.5" stroke="currentColor"/></svg>
        +55 61 8493 5710
      </li>
      <li class="contact__item">
        <span class="contact__mark"></span>
        TrabNet /marianalr
      </li>
    </ul>
    <div class="script-name">Mariana Lopes</div>
  </section>

</main>
</body>
</html>
```